Software company WebSite Design (enterprise level SW, Mobile apps, HW prototypes)

We need design for our new webpages. We got new logo and new business cards and we need webdesign which will be match with those two.
We are dealing with corporate level software development - enterprise level portals, development of optimalization SW, route planning optimalizations. For a few months we are developing mobile applications for companies.
IMPORTANT is to express the cutting edge technological company.

Target Market(s)

IT company customers

Industry/Entity Type

Business

Number of Pages Required

2 page

Requirements
Must have
• Project needs to have landing page and product detail page. Design needs to be created including full font and example images as there would be a real webpage. Design should be clean, modern and expressing hi-tech level of the company.
• Example of well designer web pages - www.quolvent.com, www.brandovi.com - We like the font formatting and font designs (colors, placing, etc - its professional).
• Attached image contains screenshot from old web landing page. It contains basic sections of our business (Simulation Tools, Enterprise Intranet Systems, Hi-tech web presentations, Supporting Enterprise services - Optimalization and logistics monitoring)

```html
<!DOCTYPE html>
<html lang="en">
<head>
<meta charset="utf-8">
<title>Korvane Solutions</title>
<link rel="stylesheet" href="https://fonts.googleapis.com/css2?family=Roboto+Condensed:wght@300;400;700&family=Open+Sans:wght@400;600&display=swap">
<style>
:root{
  --orange:#f7812a;
  --dark:#1f1f1f;
  --darker:#141414;
  --ink:#333;
  --muted:#666;
  --line:#d9d9d9;
  --grey:#e6e6e6;
  --white:#fff;
}
*{margin:0;padding:0;box-sizing:border-box}
html,body{width:1200px;height:3209px;overflow:hidden;background:var(--white)}
body{position:relative;font-family:"Open Sans",Arial,sans-serif;color:var(--ink)}
.abs{position:absolute}
.heading{font-family:"Roboto Condensed",Arial,sans-serif}
.section-title{position:absolute;left:0;width:1200px;text-align:center;font-family:"Roboto Condensed",Arial,sans-serif;font-size:28px;color:var(--orange);text-transform:uppercase}
.divider{position:absolute;left:544px;width:112px;height:12px}
.divider::before,.divider::after{content:"";position:absolute;top:6px;width:44px;height:1px;background:#bbb}
.divider::before{left:0}.divider::after{right:0}
.divider span{position:absolute;left:50%;top:0;transform:translateX(-50%);color:var(--orange);font-size:12px;line-height:12px}

/* top bar */
.topbar{top:0;left:0;width:1200px;height:26px;background:#0d0d0d;z-index:3}
.social{position:absolute;left:162px;top:7px;display:flex;gap:6px}
.social i{width:12px;height:12px;background:#555;display:block}
.top-contact{position:absolute;right:162px;top:5px;color:#ddd;font-size:11px;display:flex;gap:18px;align-items:center}
.top-contact span{display:flex;gap:6px;align-items:center}

/* hero */
.hero{top:0;left:0;width:1200px;height:560px;background:linear-gradient(100deg,#1b2a3c 0%,#2c3e52 40%,#6b7785 70%,#8d96a0 100%)}
.nav{top:38px;left:160px;width:880px;height:62px;background:rgba(20,20,20,.55);z-index:2}
.brand{position:absolute;left:14px;top:16px;display:flex;align-items:center;gap:10px;color:var(--white)}
.brand i{width:30px;height:30px;background:var(--orange);display:block}
.brand b{font-family:"Roboto Condensed",Arial,sans-serif;font-size:24px;letter-spacing:1px}
.menu{position:absolute;right:18px;top:24px;display:flex;gap:22px;font-size:11px;color:var(--white);text-transform:uppercase}
.menu .active{color:var(--orange)}
.hero-sub{top:238px;left:193px;font-family:"Roboto Condensed",Arial,sans-serif;font-weight:300;font-size:38px;color:var(--orange)}
.hero-title{top:284px;left:193px;font-family:"Roboto Condensed",Arial,sans-serif;font-weight:700;font-size:56px;color:var(--orange)}
.read-more{top:390px;left:193px;font-size:11px;color:var(--orange);padding:6px 0;border-top:1px solid var(--orange);border-bottom:1px solid var(--orange);width:86px;text-align:center}
.dots{top:268px;left:1168px;display:flex;flex-direction:column;gap:9px}
.dots i{width:7px;height:7px;border:1px solid #ccc;display:block}
.dots i.on{background:var(--orange);border-color:var(--orange)}

/* services */
.service{position:absolute;width:278px;height:166px}
.service h3{font-family:"Roboto Condensed",Arial,sans-serif;font-weight:400;font-size:18px;text-align:center;color:var(--ink);text-transform:uppercase;padding-top:14px;height:56px;border-bottom:1px solid var(--line);position:relative}
.service h3::after{content:"";position:absolute;left:50%;bottom:-3px;width:5px;height:5px;background:var(--orange);border-radius:50%;transform:translateX(-50%)}
.service .icon{position:absolute;left:20px;top:84px;width:40px;height:40px}
.service p{position:absolute;left:82px;top:80px;width:180px;font-size:11px;line-height:17px;color:var(--muted)}
.service.featured{background:var(--orange);box-shadow:0 4px 12px rgba(0,0,0,.25)}
.service.featured h3{color:var(--white);border-color:rgba(255,255,255,.5)}
.service.featured h3::after{background:var(--white)}
.service.featured p{color:var(--white)}

/* about */
.video{top:1166px;left:160px;width:428px;height:267px;background:linear-gradient(135deg,#4a4f56,#2b2f34 60%,#1b1e22)}
.video .play{position:absolute;left:196px;top:114px;width:38px;height:38px;border:2px solid var(--white);border-radius:50%}
.video .play::before,.video .play::after{content:"";position:absolute;top:10px;width:4px;height:14px;background:var(--white)}
.video .play::before{left:12px}.video .play::after{left:19px}
.video .bar{position:absolute;left:50px;right:40px;top:220px;height:3px;background:rgba(255,255,255,.4)}
.video .bar b{display:block;width:42%;height:3px;background:var(--white)}
.video .knob{position:absolute;left:175px;top:213px;width:17px;height:17px;background:var(--white);border-radius:50%}
.video .t{position:absolute;top:214px;font-size:10px;color:var(--white)}
.about{top:1174px;left:618px;width:420px;font-size:11px;line-height:18px;color:var(--muted)}
.about h4{font-size:14px;font-weight:600;color:var(--ink);margin-bottom:18px}
.about ul{list-style:none;margin-top:16px}
.about li{position:relative;padding-left:22px;margin-bottom:12px}
.about li::before{content:"";position:absolute;left:2px;top:5px;width:8px;height:5px;border-left:1.5px solid var(--muted);border-bottom:1.5px solid var(--muted);transform:rotate(-45deg)}

/* stats */
.stats{top:1489px;left:0;width:1200px;height:184px;background:linear-gradient(90deg,#202327,#33373c 50%,#1d2024)}
.stat{position:absolute;top:18px;width:150px;text-align:center;color:var(--white)}
.stat .ring{width:128px;height:128px;margin:0 auto;border:3px solid var(--white);border-radius:50%;padding:6px}
.stat .ring div{width:100%;height:100%;border:1px solid var(--white);border-radius:50%;display:flex;align-items:center;justify-content:center;font-family:"Roboto Condensed",Arial,sans-serif;font-weight:700;font-size:30px}
.stat span{display:block;margin-top:8px;font-size:12px;text-transform:uppercase}

/* process */
.process-line{top:1877px;left:261px;width:676px;height:2px;background:#555}
.step{position:absolute;top:1841px;width:120px;text-align:center}
.step .num{width:74px;height:74px;margin:0 auto;border:2px solid #555;border-radius:50%;background:var(--white);display:flex;align-items:center;justify-content:center;font-family:"Roboto Condensed",Arial,sans-serif;font-weight:300;font-size:32px;color:#444}
.step.current .num{background:var(--orange);border-color:var(--orange);color:var(--white)}
.step span{display:block;margin-top:8px;font-size:11px;text-transform:uppercase;color:var(--ink)}

/* testimonials */
.quote-photo{top:1994px;left:0;width:599px;height:440px;background:linear-gradient(135deg,#3a3a3a,#262626 55%,#1a1a1a)}
.quote-frame{top:2068px;left:66px;width:467px;height:291px;border:1px solid #bbb;padding:76px 32px 0}
.quote-frame h2{font-family:"Roboto Condensed",Arial,sans-serif;font-weight:400;font-size:30px;color:var(--white);text-transform:uppercase;margin-bottom:16px}
.quote-frame p{font-size:12px;line-height:18px;color:#eee}
.quote-panel{top:1994px;left:599px;width:601px;height:440px;background:var(--grey)}
.avatar{position:absolute;left:238px;top:75px;width:106px;height:106px;border-radius:50%;background:linear-gradient(160deg,#b08a6e,#6b4d3a);border:3px solid var(--white)}
.quote-panel p{position:absolute;left:94px;top:210px;width:414px;font-size:11px;line-height:18px;color:var(--muted);text-align:center}
.quote-panel cite{position:absolute;left:0;width:601px;top:298px;text-align:center;font-size:10px;color:var(--muted)}
.pager{position:absolute;display:flex;gap:6px}
.pager i{width:14px;height:3px;background:#555;display:block}
.pager i.on{background:var(--orange)}

/* clients */
.client{position:absolute;top:2592px;width:160px;text-align:center;color:#444}
.client i{display:block;width:34px;height:34px;margin:0 auto 6px;background:#555;border-radius:50%}
.client b{font-family:"Roboto Condensed",Arial,sans-serif;font-size:15px;text-transform:uppercase;letter-spacing:1px}

/* newsletter */
.newsletter{top:2753px;left:0;width:1200px;height:135px;background:var(--orange);color:var(--white)}
.newsletter h3{position:absolute;left:237px;top:50px;font-family:"Roboto Condensed",Arial,sans-serif;font-weight:400;font-size:21px;text-transform:uppercase}
.newsletter small{position:absolute;left:237px;top:80px;font-size:11px}
.newsletter .field{position:absolute;left:588px;top:51px;width:278px;height:37px;border:1px solid var(--white);font-size:10px;padding:12px 8px;text-transform:uppercase}
.newsletter .btn{position:absolute;left:898px;top:51px;width:114px;height:37px;border-top:1px solid var(--white);border-bottom:1px solid var(--white);font-size:11px;text-align:center;padding-top:11px;text-transform:uppercase}

/* footer */
.footer{top:2888px;left:0;width:1200px;height:267px;background:var(--dark);color:#aaa;font-size:11px}
.footer h5{position:absolute;top:42px;font-size:12px;font-weight:600;color:var(--white);text-transform:uppercase}
.footer h5::after{content:"";position:absolute;left:0;top:22px;width:28px;height:2px;background:var(--orange)}
.foot-brand{position:absolute;left:160px;top:82px;display:flex;align-items:center;gap:10px;color:var(--white)}
.foot-brand i{width:30px;height:30px;background:#777;display:block}
.foot-brand b{font-family:"Roboto Condensed",Arial,sans-serif;font-size:24px}
.foot-about{position:absolute;left:160px;top:152px;width:270px;line-height:17px}
.contact-item{position:absolute;left:462px;display:flex;gap:14px;line-height:16px}
.contact-item svg{flex:none}
.links{position:absolute;top:82px;list-style:none;line-height:29px}
.links li::before{content:"";display:inline-block;width:4px;height:4px;background:#888;border-radius:50%;margin-right:14px;vertical-align:middle}
.copyright{top:3155px;left:0;width:1200px;height:54px;background:var(--darker);color:#aaa;font-size:11px;text-align:center;padding-top:20px}
</style>
</head>
<body>

<div class="abs topbar">
  <div class="social"><i></i><i></i><i></i><i></i></div>
  <div class="top-contact">
    <span><svg width="11" height="8" viewBox="0 0 11 8"><rect x=".5" y=".5" width="10" height="7" fill="none" stroke="#ddd"/><path d="M.5 .5 5.5 4.5 10.5 .5" fill="none" stroke="#ddd"/></svg>Email Us</span>
    <span><svg width="10" height="10" viewBox="0 0 10 10"><path d="M2 0 4 3 3 4c1 2 2 3 3 3l1-1 3 2-1 2C4 10 0 6 0 1z" fill="#ddd"/></svg>(555) 014 220 7391</span>
  </div>
</div>

<div class="abs hero" role="img" aria-label="Photo of a developer working on a laptop in an office"></div>
<div class="abs nav">
  <div class="brand"><i></i><b>KORVANE</b></div>
  <div class="menu"><span class="active">Home</span><span>About</span><span>Services</span><span>Portfolio</span><span>Facts</span><span>Blogs</span><span>Contact</span></div>
</div>
<div class="abs hero-sub">WE DEVELOP AWESOME</div>
<div class="abs hero-title">MOBILE APP</div>
<div class="abs read-more">READ MORE</div>
<div class="abs dots"><i></i><i></i><i class="on"></i><i></i></div>

<h2 class="section-title" style="top:608px">What we love yo do?</h2>
<div class="divider" style="top:652px"><span>+</span></div>

<div class="service" style="left:160px;top:700px">
  <h3>Web Design</h3>
  <svg class="icon" viewBox="0 0 40 40"><path d="M6 30 28 8l5 5-22 22H6z" fill="none" stroke="#444" stroke-width="3"/><path d="M8 12l20 20" stroke="#444" stroke-width="3"/></svg>
  <p>Praesent quis porta justo. Cras vestibulum lectus luctus, maximus massa a, tristique erat.</p>
</div>
<div class="service featured" style="left:460px;top:700px">
  <h3>Web Development</h3>
  <svg class="icon" viewBox="0 0 40 40"><path d="M12 10 3 20l9 10M28 10l9 10-9 10M23 6 17 34" fill="none" stroke="#fff" stroke-width="3"/></svg>
  <p>Praesent quis porta justo. Cras vestibulum lectus luctus, maximus massa a, tristique erat.</p>
</div>
<div class="service" style="left:760px;top:700px">
  <h3>Mobile App Development</h3>
  <svg class="icon" viewBox="0 0 40 40"><rect x="8" y="4" width="20" height="32" rx="3" fill="none" stroke="#444" stroke-width="3"/><circle cx="26" cy="22" r="7" fill="#444"/><circle cx="26" cy="22" r="2.5" fill="#fff"/></svg>
  <p>Praesent quis porta justo. Cras vestibulum lectus luctus, maximus massa a, tristique erat.</p>
</div>
<div class="service" style="left:160px;top:886px">
  <h3>Route Planning</h3>
  <svg class="icon" viewBox="0 0 40 40"><g stroke="#444" stroke-width="2"><path d="M20 20 8 8M20 20l14-6M20 20l-8 14M20 20l10 12"/></g><g fill="#444"><circle cx="20" cy="20" r="5"/><circle cx="8" cy="8" r="3"/><circle cx="34" cy="14" r="3"/><circle cx="12" cy="34" r="3"/><circle cx="30" cy="32" r="3"/></g></svg>
  <p>Praesent quis porta justo. Cras vestibulum lectus luctus, maximus massa a, tristique erat.</p>
</div>
<div class="service" style="left:460px;top:886px">
  <h3>Enterprise App Development</h3>
  <svg class="icon" viewBox="0 0 40 40"><circle cx="20" cy="22" r="10" fill="none" stroke="#444" stroke-width="6" stroke-dasharray="5 3"/><circle cx="20" cy="22" r="4" fill="#444"/><path d="M28 6l6 6-8 8" fill="none" stroke="#444" stroke-width="3"/></svg>
  <p>Praesent quis porta justo. Cras vestibulum lectus luctus, maximus massa a, tristique erat.</p>
</div>
<div class="service" style="left:760px;top:886px">
  <h3>Corporate Level App</h3>
  <svg class="icon" viewBox="0 0 40 40"><rect x="8" y="4" width="22" height="32" rx="3" fill="none" stroke="#444" stroke-width="3"/><circle cx="19" cy="20" r="6" fill="none" stroke="#444" stroke-width="4" stroke-dasharray="3 2"/></svg>
  <p>Praesent quis porta justo. Cras vestibulum lectus luctus, maximus massa a, tristique erat.</p>
</div>

<h2 class="section-title" style="top:1076px">Know about us</h2>
<div class="divider" style="top:1120px"><span>+</span></div>

<div class="abs video" role="img" aria-label="Video still of a business team meeting around a table">
  <div class="play"></div>
  <div class="bar"><b></b></div>
  <div class="knob"></div>
  <span class="t" style="left:10px">2:16</span>
  <span class="t" style="right:10px">5:41</span>
</div>
<div class="abs about">
  <h4>Praesent quis porta justo. Cras vestibulum lectus luctus,</h4>
  <p>In elementum, quam nec fermentum sodales, lectus neque pulvinar diam, vulputate sagittis ipsum enim ac arcu. In hac habitasse platea dictumst. Praesent blandit nulla nec mauris elementum, vitae pulvinar augue interdum. Nam ut congue urna, sit amet pretium sem.</p>
  <ul>
    <li>Class aptent taciti sociosqu ad litora torquent per conubia nostra, per inceptos himenaeos. Nulla auctor ipsum ac augue congue. In mattis mi faucibus. Praesent eget accumsan neque.</li>
    <li>Nam pellentesque sed sapien non consectetur. Donec vel molestie lectus, id elementum enim. Duis et ullamcorper augue. Donec molestie erat id quam eleifend accumsan.</li>
  </ul>
</div>

<div class="abs stats" role="img" aria-label="Dark photo backdrop of an office team">
  <div class="stat" style="left:188px"><div class="ring"><div>400+</div></div><span>Team Strength</span></div>
  <div class="stat" style="left:411px"><div class="ring"><div>100+</div></div><span>Clients Worked With</span></div>
  <div class="stat" style="left:635px"><div class="ring"><div>200+</div></div><span>Completed Projects</span></div>
  <div class="stat" style="left:862px"><div class="ring"><div>50+</div></div><span>Ongoing Projects</span></div>
</div>

<h2 class="section-title" style="top:1729px">Our work process</h2>
<div class="divider" style="top:1773px"><span>+</span></div>
<div class="abs process-line"></div>
<div class="step current" style="left:201px"><div class="num">1</div><span>Idea</span></div>
<div class="step" style="left:428px"><div class="num">2</div><span>Planning</span></div>
<div class="step" style="left:652px"><div class="num">3</div><span>Design</span></div>
<div class="step" style="left:877px"><div class="num">4</div><span>Develop</span></div>

<div class="abs quote-photo" role="img" aria-label="Dimmed photo of colleagues in a meeting"></div>
<div class="abs quote-frame">
  <h2>What our client say's</h2>
  <p>There are many variations of passages of Lorem Ipsum available, but the majority have suffered alteration in some form, by injected humour, or randomised words which don't look even slightly believable.</p>
</div>
<div class="abs quote-panel">
  <div class="avatar" role="img" aria-label="Client portrait"></div>
  <p>Lorem Ipsum is simply dummy text of the printing and typesetting industry. Lorem Ipsum has been the industry's standard dummy text ever since the 1500s, when an unknown printer took a galley of type and scrambled it to make a type specimen book.. It has survived not only</p>
  <cite>–Martin Hale CEO Nortek Infra</cite>
  <div class="pager" style="left:258px;top:333px"><i></i><i></i><i class="on"></i></div>
</div>

<h2 class="section-title" style="top:2484px">Our clients</h2>
<div class="divider" style="top:2528px"><span>+</span></div>
<div class="client" style="left:136px"><i></i><b>Company</b></div>
<div class="client" style="left:335px"><i></i><b>Company</b></div>
<div class="client" style="left:530px"><i></i><b>Company</b></div>
<div class="client" style="left:724px"><i></i><b>CompanyName</b></div>
<div class="client" style="left:906px"><i></i><b>CompanyName</b></div>
<div class="pager" style="left:580px;top:2688px"><i></i><i style="background:#3fa9dc"></i></div>

<div class="abs newsletter">
  <h3>Suscribe our newsletter</h3>
  <small>Get notified about the latest updates.</small>
  <div class="field">Your email address</div>
  <div class="btn">Suscribe</div>
</div>

<div class="abs footer">
  <h5 style="left:160px">About us</h5>
  <div class="foot-brand"><i></i><b>KORVANE</b></div>
  <p class="foot-about">Construction SRL works as international construction services company and is a leading builder in diverse and numerous market segments. Lorem ipsum dolor sit amet, consectetur adipiscing elit.</p>

  <h5 style="left:462px">Contacts</h5>
  <div class="contact-item" style="top:82px">
    <svg width="24" height="24" viewBox="0 0 24 24"><circle cx="12" cy="12" r="11" fill="none" stroke="#888"/><path d="M12 6a4 4 0 0 1 4 4c0 3-4 8-4 8s-4-5-4-8a4 4 0 0 1 4-4z" fill="#aaa"/></svg>
    <span>PO Box 4410, Harbor Lane East,<br>Fairview 2210,<br>United States.</span>
  </div>
  <div class="contact-item" style="top:150px">
    <svg width="24" height="24" viewBox="0 0 24 24"><circle cx="12" cy="12" r="11" fill="none" stroke="#888"/><path d="M9 6l2 3-1 1c.6 1.5 1.5 2.4 3 3l1-1 3 2-1 2c-4 0-9-5-9-9z" fill="#aaa"/></svg>
    <span style="padding-top:4px">(555) 014 220 7391</span>
  </div>
  <div class="contact-item" style="top:200px">
    <svg width="24" height="24" viewBox="0 0 24 24"><circle cx="12" cy="12" r="11" fill="none" stroke="#888"/><rect x="6.5" y="8.5" width="11" height="7" fill="none" stroke="#aaa"/><path d="M6.5 8.5 12 12.5l5.5-4" fill="none" stroke="#aaa"/></svg>
    <span style="padding-top:4px">info@example.com</span>
  </div>

  <h5 style="left:762px">Infomations</h5>
  <ul class="links" style="left:762px"><li>Home</li><li>Company</li><li>Certifications</li><li>Company</li><li>Core Values</li></ul>
  <ul class="links" style="left:911px"><li>Faq</li><li>Manuals</li><li>Company History</li><li>Locations</li><li>Privacy</li></ul>
</div>
<div class="abs copyright">Copyright © 2016 Korvane Solutions. All right reserved.</div>

</body>
</html>
```